Visitenkartenvorlage ändern
Zielgruppe
Eventmanagement
Aufgabenstellung
Die beiliegende Visitenkarte wäre das "perfekte" Logo für mich. Da es sich hierbei aber um eine Vorlage eines Online-Druck-Anbieters handelt, darf es leider nur für deren Drucke verwendet werden und nicht für Printwerbung, Homepage etc. Daher sollte es genügend verfremdet werden, so dass ich es verwenden kann.

```html
<!DOCTYPE html>
<html lang="de">
<head>
<meta charset="utf-8">
<title>Lumen Planung – Visitenkarte</title>
<link href="https://fonts.googleapis.com/css2?family=Cinzel:wght@400&family=Great+Vibes&display=swap" rel="stylesheet">
<style>
  :root {
    --page: #f2f2f1;
    --card: #dcdddd;
    --card-light: #e7e8e8;
    --ink: #6a6b6c;
    --ink-soft: #7c7d7e;
  }
  * { margin: 0; padding: 0; box-sizing: border-box; }
  html, body { width: 1200px; height: 824px; overflow: hidden; }
  body {
    background: var(--page);
    display: flex;
    align-items: center;
    justify-content: center;
    gap: 50px;
    font-family: "Cinzel", serif;
    color: var(--ink);
  }
  .card {
    position: relative;
    width: 540px;
    height: 350px;
    background: var(--card);
    overflow: hidden;
    box-shadow: 0 2px 10px rgba(0,0,0,0.08);
  }
  .card-texture {
    position: absolute;
    inset: 0;
    background:
      radial-gradient(ellipse at 20% 80%, var(--card-light) 0%, transparent 45%),
      radial-gradient(ellipse at 85% 25%, var(--card-light) 0%, transparent 40%),
      var(--card);
  }
  .content { position: relative; height: 100%; }

  /* Rückseite */
  .card-back .content {
    display: flex;
    flex-direction: column;
    align-items: center;
    justify-content: center;
    text-align: center;
  }
  .brand-name {
    font-size: 38px;
    letter-spacing: 2px;
    color: var(--ink);
    font-weight: 400;
  }
  .brand-mark {
    width: 14px; height: 14px;
    border-radius: 50%;
    background: var(--ink-soft);
    margin: 22px 0;
  }
  .tagline {
    font-size: 24px;
    letter-spacing: 1px;
    color: var(--ink);
  }
  .back-email {
    margin-top: 10px;
    font-size: 14px;
    letter-spacing: 1px;
    color: var(--ink-soft);
  }

  /* Vorderseite */
  .card-front .brand {
    position: absolute;
    top: 78px;
    left: 0; right: 0;
    text-align: center;
  }
  .card-front .brand-name { font-size: 32px; }
  .card-front .tagline-small {
    font-size: 12px;
    letter-spacing: 1px;
    color: var(--ink-soft);
    margin-top: 2px;
  }
  .person {
    position: absolute;
    top: 175px;
    left: 0; right: 0;
    text-align: center;
    font-family: "Great Vibes", cursive;
    font-size: 44px;
    color: var(--ink);
  }
  .phone {
    position: absolute;
    top: 26px;
    right: 28px;
    font-family: "Cinzel", serif;
    font-size: 15px;
    color: var(--ink);
  }
  .front-email {
    position: absolute;
    bottom: 26px;
    left: 28px;
    font-size: 17px;
    letter-spacing: 1px;
    color: var(--ink);
  }
</style>
</head>
<body>
  <section class="card card-back">
    <div class="card-texture" role="img" aria-label="Heller Hintergrund mit zartem Rankenornament"></div>
    <div class="content">
      <h1 class="brand-name">Lumen Planung</h1>
      <span class="brand-mark"></span>
      <p class="tagline">Events und mehr</p>
      <p class="back-email">info@lumen-planung.de</p>
    </div>
  </section>

  <section class="card card-front">
    <div class="card-texture" role="img" aria-label="Heller Hintergrund mit zartem Rankenornament"></div>
    <div class="content">
      <p class="phone">+49 151 2468013</p>
      <div class="brand">
        <h2 class="brand-name">Lumen Planung</h2>
        <p class="tagline-small">Events und mehr</p>
      </div>
      <p class="person">Marlene Vostra</p>
      <p class="front-email">info@lumen-planung.de</p>
    </div>
  </section>
</body>
</html>
```